Teachers workshop flyer

I need a flyer to inform schools of a workshop for teachers that empowers the teacher to help traumatised and disadvantaged students to engage in successful learning.

I am a teacher and educator and my info for the flyer is attached.

Target Market(s)

Principals and vice-principals who have stressed staff and students and they want things to be better in the school!

Industry/Entity Type

Teacher

```html
<!DOCTYPE html>
<html lang="en">
<head>
<meta charset="utf-8">
<title>Brain-Based Strategies for Student Success – Teacher Workshop</title>
<link rel="stylesheet" href="https://fonts.googleapis.com/css2?family=Roboto+Condensed:wght@300&family=Arimo:wght@400;700&display=swap">
<style>
  :root {
    --slate: #434c54;
    --slate-deep: #37414a;
    --panel: #f3f3f3;
    --paper: #ffffff;
    --band-grey: #8b8d90;
    --rule: #2f3840;
    --ink: #2b2f33;
    --title: #2f3840;
    --white: #ffffff;
  }
  html, body { margin: 0; padding: 0; width: 1200px; height: 960px; overflow: hidden; background: var(--paper); }
  .flyer { position: relative; width: 1200px; height: 960px; overflow: hidden; font-family: "Arimo", Arial, sans-serif; color: var(--ink); }
  .flyer-shapes { position: absolute; inset: 0; }
  .title {
    position: absolute; left: 10px; top: 66px; width: 492px; margin: 0;
    font-family: "Roboto Condensed", "Arial Narrow", sans-serif; font-weight: 300;
    font-size: 58px; line-height: 76px; text-align: center; color: var(--title);
    white-space: nowrap;
  }
  .contact { position: absolute; left: 32px; top: 396px; color: var(--white); font-size: 19px; line-height: 27px; }
  .contact b { font-weight: 700; }
  .line { position: absolute; white-space: nowrap; font-size: 14px; line-height: 18px; }
  .presenter .line { font-size: 13.5px; }
  .justify { text-align: justify; text-align-last: justify; }
  .heading { position: absolute; margin: 0; font-size: 22px; font-weight: 700; color: var(--slate-deep); white-space: nowrap; }
  .quote-mark { position: absolute; font-family: Georgia, "Times New Roman", serif; font-weight: 700; font-size: 42px; line-height: 42px; color: var(--slate-deep); }
</style>
</head>
<body>
<main class="flyer">
  <svg class="flyer-shapes" width="1200" height="960" viewBox="0 0 1200 960">
    <defs>
      <linearGradient id="groupTone" x1="0" y1="0" x2="1" y2="1">
        <stop offset="0" stop-color="#f6efe8"/>
        <stop offset="0.5" stop-color="#e9d9c9"/>
        <stop offset="1" stop-color="#c9b7a6"/>
      </linearGradient>
      <linearGradient id="boardTone" x1="0" y1="0" x2="1" y2="1">
        <stop offset="0" stop-color="#b9cbb8"/>
        <stop offset="0.55" stop-color="#93ab96"/>
        <stop offset="1" stop-color="#6f7f73"/>
      </linearGradient>
    </defs>
    <rect class="panel-light" x="0" y="0" width="1200" height="960" fill="var(--panel)"/>
    <polygon class="photo-field" points="722,31 1200,31 1200,361 442,361" fill="var(--paper)"/>
    <polygon class="band-top-light" points="96,0 470,0 440,29 66,29" fill="#e2e2e2"/>
    <polygon class="band-top-dark" points="478,0 1200,0 1200,29 450,29" fill="var(--slate)"/>
    <polygon class="corner-dark" points="0,0 86,0 0,97" fill="var(--slate)"/>
    <polygon class="corner-grey" points="0,0 30,0 0,32" fill="#9a9c9e"/>
    <line class="corner-rule" x1="100" y1="0" x2="0" y2="109" stroke="var(--rule)" stroke-width="1.3" stroke-dasharray="4 3"/>
    <rect x="610" y="50" width="560" height="280" fill="url(#groupTone)" role="img" aria-label="Photo: a group of smiling students holding folders and books"/>
    <polygon class="band-grey" points="826,330 1200,330 1200,361 795,361" fill="var(--band-grey)"/>
    <polygon class="contact-panel" points="0,361 440,361 228,611 0,611" fill="var(--slate)"/>
    <polygon class="accent" points="1059,521 1200,370 1200,521" fill="var(--slate-deep)"/>
    <polygon class="accent" points="1028,568 1200,568 1200,608 988,608" fill="var(--slate-deep)"/>
    <polygon class="accent" points="1109,960 1200,866 1200,960" fill="var(--slate-deep)"/>
    <polygon points="223,616 633,616 400,927 0,927 0,880" fill="url(#boardTone)" role="img" aria-label="Photo: three teachers giving thumbs up in front of a chalkboard"/>
    <line class="main-rule" x1="704" y1="31" x2="0" y2="861" stroke="var(--rule)" stroke-width="1.3" stroke-dasharray="5 3"/>
    <rect x="0" y="940" width="1200" height="20" fill="var(--panel)"/>
  </svg>

  <h1 class="title">BRAIN-BASED<br>STRATEGIES FOR<br>STUDENT SUCCESS</h1>

  <div class="contact">
    Call:<br>
    <b>0400 123 456</b> for more information<br>
    or to book Dan to come to your<br>
    school<br>
    www.<b>danielfairweather</b>.com.au/<br>
    studentsuccess
  </div>

  <section class="intro">
    <span class="line justify" style="left:453px;top:402px;width:654px">Contemporary teaching is a highly complex role as increasing numbers of students attend school without</span>
    <span class="line justify" style="left:433px;top:428px;width:652px">the essential ‘self-skills’ to be truly ‘school-ready’ and successful. Instead these students often seek-out</span>
    <span class="line" style="left:412px;top:453px">attention in ways that can disruptive in the classroom causing stress and frustration for teachers.</span>
    <span class="line justify" style="left:381px;top:492px;width:647px">Dan shows how and why the most effective strategies for these students are guided by a sound under-</span>
    <span class="line justify" style="left:361px;top:519px;width:644px">standing of child-development and brain-development - especially where trauma has left lasting</span>
    <span class="line" style="left:340px;top:544px">impacts. Teachers can learn how to build a student’s self-skills, without the teacher having to become a</span>
    <span class="line" style="left:320px;top:570px">therapist!</span>
  </section>

  <section class="presenter">
    <h2 class="heading" style="left:681px;top:604px">About the Presenter:</h2>
    <span class="line justify" style="left:666px;top:640px;width:499px"><b>Daniel Fairweather</b> is a Melbourne-based therapist and educator with over twenty</span>
    <span class="line justify" style="left:648px;top:665px;width:517px">years experience working with adults and young people in the area of trauma and</span>
    <span class="line justify" style="left:630px;top:692px;width:535px">recovery. Dan’s seminars are engaging and practical since teachers need effective</span>
    <span class="line justify" style="left:613px;top:717px;width:552px">strategies that will immediately translate into classroom practice. Dan has trained here</span>
    <span class="line" style="left:595px;top:743px">and overseas in the most effective behavior change strategies.</span>
  </section>

  <section class="feedback">
    <h2 class="heading" style="left:564px;top:778px">Teacher Feedback:</h2>
    <span class="quote-mark" style="left:512px;top:797px">“</span>
    <span class="line" style="left:545px;top:814px">Dan was such an engaging and energetic presenter whom I enjoyed immensely.&nbsp; His presentation</span>
    <span class="line" style="left:526px;top:837px">on the brain and take away strategies were so practical and meaningful. It was an invaluable session.</span>
    <span class="quote-mark" style="left:1174px;top:828px">”</span>
    <span class="quote-mark" style="left:483px;top:853px">“</span>
    <span class="line" style="left:516px;top:870px">My Light-bulb moments:</span>
    <span class="line" style="left:516px;top:893px">- I need to CONNECT – not correct – far more often., - Seeing negative self-talk for what it is.</span>
    <span class="line" style="left:516px;top:916px">- Using far more ‘diversions’ in the avoidance loop.</span>
    <span class="quote-mark" style="left:842px;top:912px">”</span>
  </section>
</main>
</body>
</html>
```